Letterhead

We are looking for a basic letterhead. It should include our logo, website - northpeakkitchenware.com, phone 907.418.3952, toll free 855.392.6180, and fax 907.418.5263, along with our address 4837 Birchwood Lane, Anchorage, AK 99517. I want something that will look good printed in color or black and white.

```html
<!DOCTYPE html>
<html lang="en">
<head>
<meta charset="utf-8">
<title>North Peak Kitchenware – Letterhead</title>
<link rel="stylesheet" href="https://fonts.googleapis.com/css2?family=Roboto+Slab:wght@400;700&display=swap">
<style>
  :root {
    --brand-blue: #1a35b8;
    --brand-red: #c5102a;
    --ink: #1b1b1b;
    --rule: #6f6f6f;
    --paper: #ffffff;
    --backdrop: #e9e9e9;
  }
  html, body {
    margin: 0;
    padding: 0;
    width: 957px;
    height: 1200px;
    overflow: hidden;
    background: var(--backdrop);
  }
  .letterhead {
    position: absolute;
    left: 40px;
    top: 40px;
    width: 877px;
    height: 1135px;
    background: var(--paper);
    box-shadow: 0 2px 10px rgba(0,0,0,0.18);
    font-family: "Roboto Slab", Georgia, serif;
    color: var(--ink);
    overflow: hidden;
  }
  .brand {
    position: absolute;
    left: 22px;
    top: 102px;
    display: flex;
    align-items: center;
    gap: 10px;
    margin: 0;
  }
  .brand-mark {
    width: 14px;
    height: 14px;
    background: var(--brand-red);
  }
  .brand-name {
    font-weight: 700;
    font-size: 26px;
    line-height: 32px;
    color: var(--brand-blue);
    white-space: nowrap;
  }
  .contact-list {
    position: absolute;
    left: 549px;
    top: 18px;
    margin: 0;
    padding: 0 0 0 14px;
    list-style: none;
  }
  .contact-list::before {
    content: "";
    position: absolute;
    left: 0;
    top: 6px;
    width: 1.5px;
    height: 112px;
    background: var(--rule);
  }
  .contact-list li {
    display: flex;
    align-items: center;
    gap: 5px;
    height: 30px;
    font-size: 16px;
    line-height: 1;
    white-space: nowrap;
  }
  .contact-icon {
    width: 16px;
    height: 16px;
    flex: none;
    fill: var(--brand-blue);
  }
  .address {
    position: absolute;
    left: 0;
    right: 0;
    top: 1080px;
    height: 24px;
    margin: 0;
    display: flex;
    justify-content: center;
    align-items: center;
    gap: 8px;
    font-size: 16.5px;
    line-height: 24px;
  }
  .address .pin {
    width: 13px;
    height: 17px;
    fill: var(--ink);
  }
  .footer-band {
    position: absolute;
    left: 0;
    bottom: 0;
    width: 877px;
    height: 22px;
  }
  .band-red { fill: var(--brand-red); }
  .band-blue { fill: var(--brand-blue); }
</style>
</head>
<body>
  <main class="letterhead">
    <header>
      <p class="brand">
        <span class="brand-mark"></span>
        <span class="brand-name">North Peak Kitchenware</span>
      </p>
      <ul class="contact-list">
        <li>
          <svg class="contact-icon" viewBox="0 0 16 16" aria-hidden="true"><circle cx="8" cy="8" r="7.2" fill="none" style="stroke:var(--brand-blue)" stroke-width="1.2"/><path d="M5.2 3.8l1.6-.3.8 2-1 .8c.4 1.2 1.2 2.2 2.3 2.8l.9-.9 2 .9-.4 1.6c-3.4.3-6.8-3.4-6.2-6.9z"/></svg>
          <span>907.418.3952</span>
        </li>
        <li>
          <svg class="contact-icon" viewBox="0 0 16 16" aria-hidden="true"><circle cx="8" cy="8" r="7.2" fill="none" style="stroke:var(--brand-blue)" stroke-width="1.2"/><path d="M5.2 3.8l1.6-.3.8 2-1 .8c.4 1.2 1.2 2.2 2.3 2.8l.9-.9 2 .9-.4 1.6c-3.4.3-6.8-3.4-6.2-6.9z"/></svg>
          <span>855.392.6180 (TF)</span>
        </li>
        <li>
          <svg class="contact-icon" viewBox="0 0 16 16" aria-hidden="true"><rect x="4" y="2" width="8" height="5" rx="0.5"/><rect x="1" y="6.5" width="14" height="6" rx="1.5"/><rect x="4" y="11" width="8" height="3" fill="#fff"/><rect x="4.6" y="11.5" width="6.8" height="2.5"/></svg>
          <span>907.418.5263</span>
        </li>
        <li>
          <svg class="contact-icon" viewBox="0 0 16 16" aria-hidden="true"><circle cx="8" cy="8" r="6.5"/><path d="M1.5 8h13M8 1.5v13M3 4.5h10M3 11.5h10" stroke="#fff" stroke-width="0.8" fill="none"/><ellipse cx="8" cy="8" rx="3" ry="6.5" fill="none" stroke="#fff" stroke-width="0.8"/></svg>
          <span>www.northpeakkitchenware.com</span>
        </li>
      </ul>
    </header>

    <footer>
      <p class="address">
        <svg class="pin" viewBox="0 0 13 17" aria-hidden="true"><path d="M6.5 0C2.9 0 0 2.8 0 6.3 0 10.8 6.5 17 6.5 17S13 10.8 13 6.3C13 2.8 10.1 0 6.5 0zm0 8.8a2.5 2.5 0 1 1 0-5 2.5 2.5 0 0 1 0 5z"/></svg>
        <span>4837 Birchwood Lane, Anchorage, AK 99517</span>
      </p>
      <svg class="footer-band" viewBox="0 0 877 22" preserveAspectRatio="none" aria-hidden="true">
        <polygon class="band-red" points="0,0 420,0 378,22 0,22"/>
        <polygon class="band-blue" points="432,0 877,0 877,22 390,22"/>
      </svg>
    </footer>
  </main>
</body>
</html>
```